Business Card Design

We are a flooring/granite/cabinet company
want a sleek and modern design card. Will send our logo. maybe our logo in 3d on card.
black card

Industry/Entity Type

Business

Contact Information for Business Card

Gregory Tallis
company name Stone Hearth Depot
4827 fm 71s 78540
210-634-8872
stonehearthdepot@mailvista.example

```html
<!DOCTYPE html>
<html lang="en">
<head>
<meta charset="utf-8">
<title>Stone Hearth Depot — Business Card</title>
<link rel="stylesheet" href="https://fonts.googleapis.com/css2?family=Roboto:wght@300;400;700&display=swap">
<style>
  :root {
    --page-bg: #e6e3de;
    --card-white: #fbfbfa;
    --granite-deep: #0d121b;
    --granite-mid: #1f2835;
    --granite-fleck: #3a4757;
    --brand-blue: #1d4f78;
    --ink: #1a1a1a;
    --paper-text: #ffffff;
  }
  * { box-sizing: border-box; margin: 0; padding: 0; }
  html, body {
    width: 1200px; height: 901px; overflow: hidden;
    background: var(--page-bg);
    font-family: "Roboto", sans-serif;
  }
  .sheet {
    width: 1200px; height: 901px;
    display: flex; flex-direction: column;
    align-items: center; justify-content: center; gap: 56px;
  }
  .card {
    position: relative;
    width: 540px; height: 308px;
    border-radius: 3px;
    overflow: hidden;
    box-shadow: 0 6px 18px rgba(0,0,0,0.18);
  }
  .granite-fill {
    position: absolute;
    background:
      radial-gradient(ellipse at 30% 40%, var(--granite-fleck) 0%, transparent 55%),
      radial-gradient(ellipse at 75% 70%, var(--granite-mid) 0%, transparent 60%),
      var(--granite-deep);
  }

  /* Front */
  .card--front { background: var(--card-white); }
  .brand-lockup {
    position: absolute; top: 52px; right: 60px;
    display: flex; align-items: center; gap: 14px;
  }
  .brand-name {
    font-weight: 700; font-size: 27px; letter-spacing: 1px;
    text-transform: uppercase; color: var(--brand-blue);
  }
  .brand-mark {
    width: 22px; height: 22px; background: var(--brand-blue);
  }
  .name-band {
    top: 122px; left: 0; width: 100%; height: 48px;
  }
  .holder-name {
    position: absolute; top: 122px; right: 96px; height: 48px;
    display: flex; align-items: center;
    font-weight: 300; font-size: 21px; color: var(--paper-text);
    letter-spacing: 0.5px;
  }
  .contact-list {
    position: absolute; top: 196px; right: 96px;
    list-style: none; text-align: right;
    font-size: 14px; line-height: 21px; color: var(--ink);
  }

  /* Back */
  .card--back .granite-fill { inset: 0; }
  .back-lockup {
    position: absolute; inset: 0;
    display: flex; flex-direction: column; align-items: center; justify-content: center; gap: 18px;
  }
  .back-mark { width: 34px; height: 34px; background: var(--paper-text); }
  .back-name {
    font-weight: 700; font-size: 34px; letter-spacing: 2px;
    text-transform: uppercase; color: var(--paper-text);
  }
</style>
</head>
<body>
<main class="sheet">
  <section class="card card--front" aria-label="Business card front">
    <div class="brand-lockup">
      <span class="brand-name">Stone Hearth Depot</span>
      <span class="brand-mark"></span>
    </div>
    <div class="granite-fill name-band" role="img" aria-label="Dark granite stone texture band"></div>
    <p class="holder-name">Gregory Tallis</p>
    <ul class="contact-list">
      <li>210-634-8872</li>
      <li>4827 fm 71s 78540</li>
      <li>stonehearthdepot@mailvista.example</li>
    </ul>
  </section>

  <section class="card card--back" aria-label="Business card back">
    <div class="granite-fill" role="img" aria-label="Dark granite stone texture background"></div>
    <div class="back-lockup">
      <span class="back-mark"></span>
      <span class="back-name">Stone Hearth Depot</span>
    </div>
  </section>
</main>
</body>
</html>
```